Bookkeeping website design

We need a basic site design for wordpress.
We are a bookkeeping business and will need to present a look consistent with the colours and style of the logo.

Target Market(s)

Business owners

Industry/Entity Type

plain partner badge/Bookkeeping

Coding

Coded - Design and coding required

Number of Pages Required

1 page

```html
<!DOCTYPE html>
<html lang="en">
<head>
<meta charset="utf-8">
<title>Ledgerline Bookkeeping</title>
<link rel="stylesheet" href="https://fonts.googleapis.com/css2?family=Josefin+Sans:wght@600;700&family=Jost:wght@400;500;600&display=swap">
<style>
:root{
  --green:#93c83a;
  --blue:#1cb5ec;
  --ink:#1c1c1c;
  --text:#555;
  --muted:#888;
  --card:#f3f3f3;
  --dark:#1f1f1f;
  --white:#fff;
}
*{margin:0;padding:0;box-sizing:border-box}
html,body{width:1200px;height:4552px;overflow:hidden}
body{position:relative;background:var(--white);font-family:"Jost",sans-serif;color:var(--text);font-size:11px;line-height:1.65}
.abs{position:absolute}
.h-title{font-family:"Josefin Sans",sans-serif;font-weight:700;color:var(--ink)}
.btn{position:absolute;display:flex;align-items:center;justify-content:center;background:var(--blue);color:var(--white);border-radius:20px;font-size:11px}
.photo{position:absolute}
/* header */
.brand{position:absolute;left:125px;top:40px;font-family:"Jost",sans-serif;font-weight:600;font-size:20px;color:var(--green);line-height:1.1;display:flex;align-items:center;gap:10px}
.brand-dot{width:26px;height:26px;border-radius:50%;background:var(--green);flex:none}
.nav{position:absolute;top:48px;font-size:11px;color:#333}
.nav.active{color:var(--green)}
.nav.active::after{content:"";position:absolute;left:0;right:0;bottom:-4px;height:2px;background:var(--green)}
.quote{position:absolute;left:930px;top:40px;width:138px;height:35px;border-radius:18px;background:linear-gradient(90deg,var(--blue) 70%,var(--green) 70%);color:var(--white);font-weight:600;font-size:11px;display:flex;align-items:center;padding-left:20px}
/* hero */
.hero{position:absolute;left:0;top:113px;width:1200px;height:672px;background:linear-gradient(100deg,#7d6a5c 0%,#a89888 35%,#d9d4cf 65%,#bfc3c6 100%)}
.hero h1{position:absolute;left:130px;top:235px;font-family:"Josefin Sans",sans-serif;font-weight:700;font-size:47px;line-height:1.25;color:var(--white);letter-spacing:1px}
.hero .bar{position:absolute;left:105px;top:240px;width:3px;height:102px;background:var(--blue)}
.hero p{position:absolute;left:135px;top:360px;width:390px;color:var(--white);font-size:11px}
.play{position:absolute;left:275px;top:420px;width:32px;height:32px;border-radius:50%;background:var(--green)}
.watch{position:absolute;left:316px;top:428px;color:var(--white);font-size:11px}
.slide-no{position:absolute;left:1108px;top:294px;color:var(--white);font-size:10px}
/* about */
.about-img{left:163px;top:918px;width:440px;height:387px;background:linear-gradient(135deg,#c9b7a3,#e9ecef 50%,#8fa6bd)}
.green-corner{position:absolute;left:518px;top:912px;width:92px;height:8px;background:var(--green)}
.green-corner2{position:absolute;left:602px;top:912px;width:8px;height:92px;background:var(--green)}
.sec-line{position:absolute;height:3px;width:55px;background:var(--blue)}
.check{position:absolute;display:flex;align-items:center;gap:8px;font-size:11px;color:#333;font-weight:500}
.check svg{flex:none}
/* services */
.card{position:absolute;width:296px;height:257px;background:var(--card);text-align:center}
.card.on{background:var(--green)}
.card svg{position:absolute;left:118px;top:45px}
.card h3{position:absolute;top:125px;left:0;right:0;font-family:"Jost",sans-serif;font-weight:500;font-size:14px;color:var(--ink);letter-spacing:.3px}
.card .ul{position:absolute;top:152px;left:129px;width:38px;height:2px;background:var(--blue)}
.card p{position:absolute;top:162px;left:38px;right:38px;font-size:10.5px}
.card.on h3,.card.on p{color:var(--white)}
.card.on .ul{background:var(--white)}
/* blog */
.post{position:absolute;width:296px;height:332px;border:1px solid #eee;background:var(--white)}
.post .pic{position:absolute;left:10px;top:8px;right:10px;height:168px}
.post .date{position:absolute;left:18px;top:16px;width:30px;height:42px;background:var(--blue);color:var(--white);font-size:9px;line-height:1.2;padding:8px 0 0 6px}
.post h4{position:absolute;left:10px;top:190px;font-size:11px;font-weight:600;color:var(--ink)}
.post p{position:absolute;left:10px;top:220px;right:8px;font-size:10.5px}
.post a{position:absolute;left:10px;top:290px;font-size:10.5px;color:var(--blue);text-decoration:underline}
.partner{position:absolute;top:3468px;width:176px;height:137px;border:1px solid #e6e6e6}
.partner span{position:absolute;left:58px;top:38px;width:60px;height:60px;background:#d8d8d8;border-radius:6px}
/* contact */
.field{position:absolute;border:1px solid #eee;font-size:10px;color:#999;padding:10px 8px}
/* footer */
.footer{position:absolute;left:0;top:4156px;width:1200px;height:332px;background:var(--dark);color:#ddd}
.footer h5{position:absolute;font-size:11px;font-weight:600;color:var(--white);letter-spacing:.5px}
.panel{position:absolute;left:490px;top:4146px;width:228px;height:276px;background:#f4f4f4;clip-path:polygon(12px 0,216px 0,228px 12px,228px 100%,0 100%,0 12px)}
.soc{position:absolute;top:4342px;width:28px;height:28px;border-radius:50%;background:#222}
.soc.g{background:var(--green)}
.fnav{position:absolute;top:4444px;left:0;width:1200px;text-align:center;font-size:10.5px;color:var(--white)}
.fnav b{font-weight:600}
</style>
</head>
<body>

<header>
  <div class="brand"><span class="brand-dot"></span>Ledgerline<br>Bookkeeping</div>
  <span class="nav active" style="left:474px">Home</span>
  <span class="nav" style="left:540px">About us</span>
  <span class="nav" style="left:621px">Our Services</span>
  <span class="nav" style="left:722px">Team</span>
  <span class="nav" style="left:784px">Blog</span>
  <span class="nav" style="left:841px">Contact us</span>
  <div class="quote">Get A Quote
    <svg class="abs" style="left:98px;top:12px" width="32" height="12" viewBox="0 0 32 12"><path d="M0 6H29M24 1l5 5-5 5" stroke="#fff" stroke-width="1.6" fill="none"/></svg>
  </div>
</header>

<section class="hero" role="img" aria-label="Smiling businesswoman with glasses at a desk writing on papers">
  <div class="bar"></div>
  <h1>Helps You To<br>Company Grow</h1>
  <p>Lorem Ipsum is simply dummy text of the printing and typesetting industry has been the industry's standard dummy text ever since the 1500s.</p>
  <div class="btn" style="left:135px;top:420px;width:127px;height:34px">Get Started</div>
  <div class="play"><svg width="32" height="32"><path d="M13 10l9 6-9 6z" fill="#fff"/></svg></div>
  <span class="watch">Watch Video</span>
  <span class="slide-no">02</span>
  <svg class="abs" style="left:1128px;top:290px" width="36" height="24"><path d="M4 2H36M0 12H36M4 22H36" stroke="#fff" stroke-width="1.2"/></svg>
</section>

<section class="about">
  <div class="green-corner"></div><div class="green-corner2"></div>
  <div class="photo about-img" role="img" aria-label="Two people reviewing financial charts with a calculator and pen"></div>
  <h2 class="h-title abs" style="left:664px;top:915px;font-size:28px">ABOUT US</h2>
  <div class="sec-line" style="left:666px;top:956px"></div>
  <p class="abs" style="left:666px;top:988px;width:410px;font-size:10.5px">Lorem Ipsum is simply dummy text of the printing and typesetting industry has been the industry's standard dummy text ever since the 1500s.</p>
  <p class="abs" style="left:666px;top:1042px;width:410px;font-size:10.5px">when an unknown printer took a galley of type and scrambled it to make a type specimen book. It has survived not only five centuries, but also the leap into electronic typesetting, remaining essentially unchanged. It was popularised in the 1960s</p>
  <div class="check" style="left:666px;top:1156px"><svg width="17" height="17"><circle cx="8.5" cy="8.5" r="7.5" stroke="#93c83a" fill="none"/><path d="M5 9l2.5 2.5L12 6" stroke="#93c83a" stroke-width="1.6" fill="none"/></svg>Professional Team</div>
  <div class="check" style="left:666px;top:1186px"><svg width="17" height="17"><circle cx="8.5" cy="8.5" r="7.5" stroke="#93c83a" fill="none"/><path d="M5 9l2.5 2.5L12 6" stroke="#93c83a" stroke-width="1.6" fill="none"/></svg>High Savings Potential</div>
  <div class="check" style="left:666px;top:1216px"><svg width="17" height="17"><circle cx="8.5" cy="8.5" r="7.5" stroke="#93c83a" fill="none"/><path d="M5 9l2.5 2.5L12 6" stroke="#93c83a" stroke-width="1.6" fill="none"/></svg>24/7 customer Support</div>
  <div class="check" style="left:870px;top:1156px"><svg width="17" height="17"><circle cx="8.5" cy="8.5" r="7.5" stroke="#93c83a" fill="none"/><path d="M5 9l2.5 2.5L12 6" stroke="#93c83a" stroke-width="1.6" fill="none"/></svg>Expert Adviser</div>
  <div class="check" style="left:870px;top:1186px"><svg width="17" height="17"><circle cx="8.5" cy="8.5" r="7.5" stroke="#93c83a" fill="none"/><path d="M5 9l2.5 2.5L12 6" stroke="#93c83a" stroke-width="1.6" fill="none"/></svg>High Savings Potential</div>
  <div class="check" style="left:870px;top:1216px"><svg width="17" height="17"><circle cx="8.5" cy="8.5" r="7.5" stroke="#93c83a" fill="none"/><path d="M5 9l2.5 2.5L12 6" stroke="#93c83a" stroke-width="1.6" fill="none"/></svg>24/7 customer Support</div>
  <div class="btn" style="left:667px;top:1270px;width:130px;height:33px">Read More</div>
</section>

<section class="services">
  <h2 class="h-title abs" style="left:0;width:1200px;text-align:center;top:1412px;font-size:28px">OUR SERVICES</h2>
  <p class="abs" style="left:0;width:1200px;text-align:center;top:1448px;font-size:10.5px;color:#444">What We Provide</p>

  <div class="card" style="left:133px;top:1490px">
    <svg width="60" height="60" viewBox="0 0 60 60" fill="none" stroke="#222" stroke-width="2"><path d="M8 8H52M12 8V38H48V8M30 38V46M22 54l8-8 8 8M20 18l6 6M26 18l-6 6M38 18l4 4M42 18l-4 4M22 30c6-4 12-6 18-10"/></svg>
    <h3>STRATEGIC PLANNING</h3><div class="ul"></div>
    <p>Lorem Ipsum is simply dummy text of the printing and typesetting industry has been the industry's standard.</p>
  </div>
  <div class="card on" style="left:453px;top:1490px">
    <svg width="60" height="60" viewBox="0 0 60 60" fill="none" stroke="#fff" stroke-width="2"><path d="M14 6H40L46 12V54H14Z"/><text x="18" y="24" font-family="Jost" font-size="11" font-weight="600" fill="#fff" stroke="none">TAX</text><path d="M18 32H34M18 38H30M18 44H30"/><circle cx="44" cy="42" r="9"/><path d="M40 38l8 8M48 38l-8 8"/></svg>
    <h3>INSURANCE TAX</h3><div class="ul"></div>
    <p>Lorem Ipsum is simply dummy text of the printing and typesetting industry has been the industry's standard.</p>
  </div>
  <div class="card" style="left:772px;top:1490px">
    <svg width="60" height="60" viewBox="0 0 60 60" fill="none" stroke="#222" stroke-width="2"><path d="M10 22a20 16 0 0 1 40 0c-4-3-8-3-10 0-3-3-7-3-10 0-3-3-7-3-10 0-3-3-7-3-10 0zM30 22V34"/><circle cx="19" cy="44" r="9"/><circle cx="41" cy="44" r="9"/><text x="15" y="49" font-size="12" fill="#222" stroke="none">$</text><text x="37" y="49" font-size="12" fill="#222" stroke="none">$</text></svg>
    <h3>FINANCE SECURE</h3><div class="ul"></div>
    <p>Lorem Ipsum is simply dummy text of the printing and typesetting industry has been the industry's standard.</p>
  </div>
  <div class="card" style="left:133px;top:1772px">
    <svg width="60" height="60" viewBox="0 0 60 60" fill="none" stroke="#222" stroke-width="2"><circle cx="18" cy="14" r="5"/><path d="M12 54V34l-6-6M18 22v32M24 34V26l10-6"/><path d="M32 54V44H38V54M42 54V38H48V54M52 54V30"/><circle cx="46" cy="14" r="7"/><text x="42" y="18" font-size="10" fill="#222" stroke="none">$</text></svg>
    <h3>FINANCE PLANNING</h3><div class="ul"></div>
    <p>Lorem Ipsum is simply dummy text of the printing and typesetting industry has been the industry's standard.</p>
  </div>
  <div class="card" style="left:453px;top:1772px">
    <svg width="60" height="60" viewBox="0 0 60 60" fill="none" stroke="#222" stroke-width="2"><path d="M10 14H38V56H10Z"/><path d="M16 22H32V30H16ZM16 36h4v4h-4zM24 36h4v4h-4zM16 44h4v4h-4zM24 44h4v4h-4z"/><circle cx="44" cy="14" r="10"/><path d="M44 8V14L48 17"/></svg>
    <h3>PROJECT MANAGEMENT</h3><div class="ul"></div>
    <p>Lorem Ipsum is simply dummy text of the printing and typesetting industry has been the industry's standard.</p>
  </div>
  <div class="card" style="left:772px;top:1772px">
    <svg width="60" height="60" viewBox="0 0 60 60" fill="none" stroke="#222" stroke-width="2"><path d="M14 6H38L44 12V50H14Z"/><path d="M20 18H36M20 24H36M20 30H30M20 38l4 4 6-6"/><circle cx="40" cy="42" r="7"/><path d="M45 47l7 7"/></svg>
    <h3>ASSURANCY &amp; AUDIT</h3><div class="ul"></div>
    <p>Lorem Ipsum is simply dummy text of the printing and typesetting industry has been the industry's standard.</p>
  </div>
</section>

<section class="specialized">
  <div class="photo" style="left:480px;top:2152px;width:720px;height:608px;background:linear-gradient(135deg,#f1efe9,#d6dde2 45%,#a9c2c8 70%,#e6e8ea)" role="img" aria-label="Hands using a tablet showing sales analytics charts over printed reports"></div>
  <svg class="abs" style="left:0;top:2152px" width="700" height="656" viewBox="0 0 700 656">
    <path d="M0 20H668C640 20 628 40 620 60L470 560C455 610 420 620 380 620H0Z" fill="#93c83a"/>
    <path d="M0 636H420C445 636 460 620 472 600" stroke="#1cb5ec" stroke-width="8" fill="none"/>
  </svg>
  <div class="abs" style="left:103px;top:2340px;width:3px;height:96px;background:var(--blue)"></div>
  <h2 class="abs" style="left:132px;top:2332px;font-family:'Josefin Sans',sans-serif;font-weight:700;font-size:36px;line-height:1.2;color:#fff">We are specialized<br>in bookkeeping</h2>
  <p class="abs" style="left:135px;top:2450px;width:340px;color:#fff;font-size:10.5px">Lorem Ipsum is simply dummy text of the printing and typesetting industry has been the industry's standard dummy text ever since the 1500s.</p>
  <div class="check" style="left:133px;top:2520px;color:#fff"><svg width="17" height="17"><circle cx="8.5" cy="8.5" r="7.5" stroke="#fff" fill="none"/><path d="M5 9l2.5 2.5L12 6" stroke="#fff" stroke-width="1.6" fill="none"/></svg>Expert Adviser</div>
  <div class="check" style="left:133px;top:2550px;color:#fff"><svg width="17" height="17"><circle cx="8.5" cy="8.5" r="7.5" stroke="#fff" fill="none"/><path d="M5 9l2.5 2.5L12 6" stroke="#fff" stroke-width="1.6" fill="none"/></svg>High Savings Potential</div>
  <div class="check" style="left:133px;top:2580px;color:#fff"><svg width="17" height="17"><circle cx="8.5" cy="8.5" r="7.5" stroke="#fff" fill="none"/><path d="M5 9l2.5 2.5L12 6" stroke="#fff" stroke-width="1.6" fill="none"/></svg>24/7 customer Support</div>
  <div class="btn" style="left:135px;top:2628px;width:127px;height:32px">Get Started</div>
</section>

<section class="blog">
  <h2 class="h-title abs" style="left:0;width:1200px;text-align:center;top:2890px;font-size:28px">OUR BLOG</h2>
  <p class="abs" style="left:0;width:1200px;text-align:center;top:2926px;font-size:10.5px;color:#444">Latest Blog &amp; Articales</p>
  <article class="post" style="left:122px;top:2968px">
    <div class="pic" style="background:linear-gradient(135deg,#eae6e2,#c9c3c0 60%,#f2d9d6)" role="img" aria-label="Calculator beside a laptop showing a payroll screen"></div>
    <div class="date">02<br>Mar</div>
    <h4>Filling Payroll Taxes</h4>
    <p>Lorem Ipsum is simply dummy text of the printing and typesetting industry has been the industry's standard dummy text ever since the 1500s.</p>
    <a>Read More</a>
  </article>
  <article class="post" style="left:450px;top:2968px">
    <div class="pic" style="background:linear-gradient(135deg,#3b3a38,#8d8a86 50%,#d9dde0)" role="img" aria-label="Person in a suit writing over financial charts with glasses on the desk"></div>
    <div class="date">02<br>Mar</div>
    <h4>Finance Planning</h4>
    <p>Lorem Ipsum is simply dummy text of the printing and typesetting industry has been the industry's standard dummy text ever since the 1500s.</p>
    <a>Read More</a>
  </article>
  <article class="post" style="left:778px;top:2968px">
    <div class="pic" style="background:linear-gradient(135deg,#1d3a5a,#4f86b3 50%,#1b2b3e)" role="img" aria-label="Businessman touching a glowing digital finance display"></div>
    <div class="date">02<br>Mar</div>
    <h4>Good Tax Planning</h4>
    <p>Lorem Ipsum is simply dummy text of the printing and typesetting industry has been the industry's standard dummy text ever since the 1500s.</p>
    <a>Read More</a>
  </article>
  <div class="btn" style="left:535px;top:3330px;width:138px;height:35px">View More</div>
</section>

<section class="partners">
  <h2 class="h-title abs" style="left:0;width:1200px;text-align:center;top:3422px;font-size:28px">OUR PARTNER</h2>
  <div class="partner" style="left:131px"><span></span></div>
  <div class="partner" style="left:321px"><span></span></div>
  <div class="partner" style="left:511px"><span></span></div>
  <div class="partner" style="left:701px"><span></span></div>
  <div class="partner" style="left:891px"><span></span></div>
  <svg class="abs" style="left:584px;top:3633px" width="32" height="8"><circle cx="4" cy="4" r="3" fill="none" stroke="#1cb5ec"/><circle cx="16" cy="4" r="3" fill="#93c83a"/><circle cx="28" cy="4" r="3" fill="none" stroke="#1cb5ec"/></svg>
</section>

<section class="contact">
  <h2 class="abs" style="left:131px;top:3737px;font-family:'Jost',sans-serif;font-weight:500;font-size:22px;color:var(--ink)">Quick Contact</h2>
  <div class="abs" style="left:133px;top:3782px;width:38px;height:2px;background:var(--green)"></div>
  <div class="field" style="left:133px;top:3805px;width:217px;height:57px">Name*</div>
  <div class="field" style="left:133px;top:3868px;width:217px;height:57px">Phone*</div>
  <div class="field" style="left:133px;top:3931px;width:217px;height:57px">Email*</div>
  <div class="field" style="left:358px;top:3805px;width:217px;height:183px">Message</div>
  <div class="btn" style="left:135px;top:4010px;width:145px;height:35px">Send</div>
  <div class="photo" style="left:621px;top:3740px;width:446px;height:310px;background:linear-gradient(135deg,#eef1f3,#9aa3ab 55%,#56606a)" role="img" aria-label="Hands typing on a laptop beside a calculator"></div>
</section>

<footer>
  <div class="footer">
    <h5 style="left:190px;top:80px">CONTACT INFO</h5>
    <div class="abs" style="left:190px;top:100px;width:34px;height:2px;background:var(--green)"></div>
    <svg class="abs" style="left:190px;top:135px" width="10" height="10"><path d="M2 1l2 0 1 3-1 1c1 2 2 3 4 4l1-1 3 1v2c-5 0-10-5-10-10z" fill="#1cb5ec"/></svg>
    <span class="abs" style="left:210px;top:128px;font-size:10px">+00 555 201 4470</span>
    <svg class="abs" style="left:190px;top:154px" width="10" height="8"><rect x="0" y="0" width="10" height="8" fill="#1cb5ec"/><path d="M0 0l5 4 5-4" stroke="#1f1f1f" fill="none"/></svg>
    <span class="abs" style="left:210px;top:147px;font-size:10px">hello@ledgerline.example</span>
    <svg class="abs" style="left:190px;top:188px" width="9" height="12"><path d="M4.5 0a4.5 4.5 0 0 1 4.5 4.5C9 8 4.5 12 4.5 12S0 8 0 4.5A4.5 4.5 0 0 1 4.5 0z" fill="#1cb5ec"/></svg>
    <span class="abs" style="left:210px;top:182px;font-size:10px;line-height:1.8">48 Orchard Lane,<br>Millbrook, NY 10000</span>

    <h5 style="left:868px;top:80px">NEWSLETTER</h5>
    <div class="abs" style="left:868px;top:100px;width:34px;height:2px;background:var(--green)"></div>
    <p class="abs" style="left:868px;top:112px;width:200px;font-size:10.5px">Enter Your Email Address here to be updated.</p>
    <div class="abs" style="left:870px;top:156px;width:197px;height:28px;border-radius:14px;background:#fff;color:#666;font-size:10px;padding:6px 16px">Email Address</div>
    <div class="btn" style="left:870px;top:195px;width:118px;height:29px">Subscribe</div>
  </div>
  <div class="panel">
    <div class="abs" style="left:20px;top:100px;width:188px;display:flex;align-items:center;gap:8px;font-family:'Jost',sans-serif;font-weight:600;font-size:17px;color:var(--green);line-height:1.1"><span class="brand-dot"></span>Ledgerline<br>Bookkeeping</div>
  </div>
  <span class="soc g" style="left:518px"></span>
  <span class="soc" style="left:559px"></span>
  <span class="soc" style="left:601px"></span>
  <span class="soc" style="left:642px"></span>
  <div class="fnav"><b>Home</b> &nbsp; | &nbsp; About us &nbsp; | &nbsp; Our Services &nbsp; | &nbsp; Team &nbsp; | &nbsp; Blog &nbsp; | &nbsp; Contact us</div>
  <span class="abs" style="left:133px;top:4510px;font-size:10px;color:#444">© 2021 <span style="color:var(--green)">Ledgerline Bookkeeping</span> . All Rights Reserved.</span>
  <span class="abs" style="left:887px;top:4510px;width:180px;text-align:right;font-size:10px;color:#444">Privacy Policy | Term &amp; Conditions</span>
</footer>

</body>
</html>
```